VANTRELL INSULATION STATIONARY
BUSINESS CARDS,STATIONARY,ENVELOPES & T-SHIRTS
Modern
ED VANTRELL
OWNER,SALES
14 BRISTLECONE CT. CHICO,CA. 95928
VANTRELLINSULATION@MAILNEST.EXAMPLE
WWW.VANTRELLINSULATION.EXAMPLE
I'M GOING TO GET A WEBSITE DESIGN HERE TOO,THATS WHY I'M USING THE WEBSITE ADDRESS,PROBABLY MY E-MAIL IS GOING TO CHANGE AFTER I GET THE WEBSITE,BUT I THINK THIS IS EASY TO CHANGE.

```html
<!DOCTYPE html>
<html lang="en">
<head>
<meta charset="utf-8">
<title>Vantrell Insulation – Business Card</title>
<link rel="stylesheet" href="https://fonts.googleapis.com/css2?family=Questrial&display=swap">
<style>
  :root {
    --green-deep: #0f5a1c;
    --green-mid: #2e8a25;
    --green-bright: #5fb12d;
    --lime: #8cc63f;
    --lime-light: #b5dc4a;
    --ink: #1e1e1e;
    --muted: #555555;
    --white: #ffffff;
  }
  * { margin: 0; padding: 0; box-sizing: border-box; }
  html, body {
    width: 1200px;
    height: 679px;
    overflow: hidden;
    background: var(--white);
  }
  .card {
    position: relative;
    width: 1200px;
    height: 679px;
    background: var(--white);
    font-family: "Questrial", "Century Gothic", sans-serif;
    color: var(--ink);
    overflow: hidden;
  }
  .top-band {
    position: absolute;
    left: 0; top: 0;
    width: 100%; height: 74px;
    background: linear-gradient(90deg, var(--green-bright) 0%, var(--green-mid) 45%, var(--green-deep) 100%);
  }
  .top-stripe {
    position: absolute;
    left: 0; top: 74px;
    width: 100%; height: 22px;
    background: linear-gradient(90deg, var(--lime-light) 0%, var(--lime) 60%, var(--green-bright) 100%);
  }
  .brand {
    position: absolute;
    left: 55px; top: 140px;
    display: flex;
    align-items: center;
    gap: 22px;
  }
  .brand-mark {
    width: 68px; height: 68px;
    background: var(--green-bright);
  }
  .brand-name {
    color: var(--green-mid);
    line-height: 1;
  }
  .brand-name .primary {
    display: block;
    font-size: 62px;
    letter-spacing: 1px;
  }
  .brand-name .secondary {
    display: block;
    margin-top: 6px;
    font-size: 33px;
    letter-spacing: 1px;
  }
  .website {
    position: absolute;
    left: 65px; top: 276px;
    font-size: 24px;
    color: var(--muted);
  }
  .person {
    position: absolute;
    left: 0; top: 330px;
    width: 1188px;
    text-align: center;
  }
  .person-name {
    color: var(--green-mid);
    font-size: 58px;
    letter-spacing: 2px;
    line-height: 1;
  }
  .person-role {
    margin-top: 4px;
    font-size: 24px;
    color: var(--muted);
  }
  .contact {
    position: absolute;
    left: 833px; top: 452px;
    font-size: 27px;
    line-height: 39px;
    color: var(--ink);
    border-collapse: collapse;
  }
  .contact td { padding: 0; }
  .contact .label { width: 115px; }
  .bottom-stripe {
    position: absolute;
    left: 0; top: 568px;
    width: 100%; height: 22px;
    background: linear-gradient(90deg, var(--lime-light) 0%, var(--lime) 60%, var(--green-bright) 100%);
  }
  .bottom-band {
    position: absolute;
    left: 0; top: 590px;
    width: 100%; height: 89px;
    background: linear-gradient(90deg, var(--green-bright) 0%, var(--green-mid) 45%, var(--green-deep) 100%);
    display: flex;
    align-items: center;
    justify-content: space-between;
    padding: 0 34px;
    color: var(--white);
    font-size: 25px;
  }
</style>
</head>
<body>
  <div class="card">
    <div class="top-band"></div>
    <div class="top-stripe"></div>

    <div class="brand">
      <div class="brand-mark"></div>
      <div class="brand-name">
        <span class="primary">VANTRELL</span>
        <span class="secondary">INSULATION</span>
      </div>
    </div>
    <div class="website">www.vantrellinsulation.example</div>

    <div class="person">
      <div class="person-name">ED VANTRELL</div>
      <div class="person-role">Owner, Sales</div>
    </div>

    <table class="contact">
      <tr><td class="label">Phone</td><td>(530) 555-0142</td></tr>
      <tr><td class="label">Cell</td><td>(530) 555-0187</td></tr>
      <tr><td class="label">Fax</td><td>(530) 555-0142</td></tr>
    </table>

    <div class="bottom-stripe"></div>
    <div class="bottom-band">
      <span class="address">address: 14 Bristlecone Ct. Chico,ca. 95928</span>
      <span class="email">email: vantrellinsulation@mailnest.example</span>
    </div>
  </div>
</body>
</html>
```